Webbanner-Design
Zielgruppe
Verkauf von Pools und Zubehör
Aufgabenstellung
Es soll ein Banner für unseren Shop sein für eine Aktion, dass Holzpools jetzt sofort lieferbar sind Text:
Verschönern Sie doch Ihren Garten: Holzpools sofort lieferbar!
Unseren Shop finden Sie unter www.brisabad17.de
Fotos können von unserer Seite www.brisabad17-gallery.de verwendet werden
Das angefügte Bild sollte ebenfalls dabei sein. Hintergrund: die Leute sollen wegen Corona zu Hause bleiben und haben Zeit, daher sind unsere sofort lieferbaren Pools jetzt natürlich gut. Ich bin auch für abweichende Texte offen.

```html
<!DOCTYPE html>
<html lang="de">
<head>
<meta charset="utf-8">
<title>Brisabad17 – Holzpools sofort lieferbar</title>
<link rel="stylesheet" href="https://fonts.googleapis.com/css2?family=Open+Sans:wght@400;600;700;800&family=Montserrat:wght@900&display=swap">
<style>
  :root{
    --cyan:#00b4e6;
    --navy:#0d1a7a;
    --navy-deep:#0a1566;
    --banner-cyan:#14b3ef;
    --text:#333;
    --muted:#555;
    --line:#e1e1e1;
    --page:#eeeeee;
    --water-a:#1a8fd0;
    --water-b:#5fc3ee;
    --white:#fff;
  }
  *{box-sizing:border-box;margin:0;padding:0}
  html,body{width:1200px;height:1023px;overflow:hidden}
  body{position:relative;background:var(--page);font-family:"Open Sans",Arial,sans-serif;color:var(--text)}
  .water-backdrop{position:absolute;left:0;top:0;width:1200px;height:577px;
    background:linear-gradient(135deg,var(--water-a),var(--water-b) 40%,var(--water-a) 70%,var(--water-b))}
  .shop{position:absolute;left:99px;top:0;width:1002px;height:1023px;background:var(--white)}
  .service-bar{height:32px;background:var(--cyan);display:flex;justify-content:space-around;align-items:center;color:var(--white);font-size:13px}
  .service-bar span{display:flex;align-items:center;gap:4px}
  .service-bar svg{width:11px;height:11px}
  .meta-links{position:absolute;right:26px;top:43px;font-size:11px;display:flex}
  .meta-links a{color:var(--text);text-decoration:none;padding:0 5px;border-left:1px solid #ccc}
  .meta-links a:first-child{border-left:none}
  .brand{position:absolute;left:24px;top:80px;display:flex;align-items:center;gap:8px;font-size:27px;font-weight:700;color:var(--cyan)}
  .brand i{width:18px;height:18px;border-radius:50%;background:var(--cyan);display:block}
  .search{position:absolute;left:548px;top:90px;width:222px;height:31px;border:1px solid #ccc;border-radius:3px;display:flex}
  .search span{flex:1;padding:6px 11px;font-size:13px;color:#999}
  .search b{width:37px;border-left:1px solid #ccc;background:#f5f5f5;display:flex;align-items:center;justify-content:center}
  .account{position:absolute;left:795px;top:98px;font-size:13px;display:flex;gap:28px}
  .account span{display:flex;align-items:center;gap:4px}
  .main-nav{position:absolute;left:0;top:175px;width:1002px;height:44px;border-top:2px solid var(--line);border-bottom:2px solid var(--line);display:flex;align-items:center;padding-left:24px;gap:24px;font-size:13.5px;color:var(--muted)}
  .caret::after{content:"";display:inline-block;margin-left:3px;border:3.5px solid transparent;border-top-color:var(--muted);vertical-align:-1px}
  .hero{position:absolute;left:20px;top:241px;width:962px;height:324px}
  .slider-dots{position:absolute;left:0;width:1002px;top:591px;display:flex;justify-content:center;gap:16px}
  .slider-dots i{width:6px;height:6px;border-radius:50%;background:#444;display:block;margin-top:2px}
  .slider-dots i.active{width:10px;height:10px;margin-top:0;background:none;border:2px solid #444}
  .divider{position:absolute;left:22px;top:642px;width:958px;border-top:1px solid var(--line)}
  .section-title{position:absolute;left:22px;top:658px;font-size:21px;font-weight:400}
  .category{position:absolute;top:756px;width:264px;text-align:center;font-size:13px}
  .category .photo{height:198px;margin-bottom:44px}
</style>
</head>
<body>
<div class="water-backdrop" role="img" aria-label="Wasseroberfläche eines Pools als Hintergrund"></div>
<div class="shop">
  <div class="service-bar">
    <span><svg viewBox="0 0 12 12"><path fill="#fff" d="M2 1l2 0 1 3-1.3 1a6 6 0 0 0 3.3 3.3L8 7l3 1v2a1 1 0 0 1-1 1A9 9 0 0 1 1 2a1 1 0 0 1 1-1z"/></svg>+49 (0) 7123 / 456 780 1</span>
    <span><svg viewBox="0 0 12 12"><rect width="12" height="12" rx="2" fill="#fff"/><path d="M3 6l2 2 4-4" stroke="#00b4e6" stroke-width="1.8" fill="none"/></svg>persönliche Beratung</span>
    <span><svg viewBox="0 0 12 12"><rect width="12" height="12" rx="2" fill="#fff"/><path d="M3 6l2 2 4-4" stroke="#00b4e6" stroke-width="1.8" fill="none"/></svg>sicher Einkaufen</span>
    <span><svg viewBox="0 0 12 12"><circle cx="6" cy="6" r="6" fill="#fff"/><path d="M3 6h5M6 3.5L8.5 6 6 8.5" stroke="#00b4e6" stroke-width="1.6" fill="none"/></svg>Brisabad-Galerie</span>
  </div>
  <nav class="meta-links"><a>Startseite</a><a>Mein Konto</a><a>Kontakt</a><a>Unsere Partner</a><a>Bildergalerie</a><a>Wir über uns</a><a>News</a></nav>
  <div class="brand"><i></i>Brisabad17</div>
  <div class="search"><span>Suchen</span><b><svg width="15" height="15" viewBox="0 0 16 16"><circle cx="6.5" cy="6.5" r="5" stroke="#00b4e6" stroke-width="2" fill="none"/><path d="M10 10l4.5 4.5" stroke="#00b4e6" stroke-width="2.4"/></svg></b></div>
  <div class="account">
    <span class="caret"><svg width="10" height="11" viewBox="0 0 10 11"><circle cx="5" cy="3" r="2.6" fill="#333"/><path d="M0 11a5 4.5 0 0 1 10 0z" fill="#333"/></svg>Anmelden</span>
    <span class="caret"><svg width="13" height="11" viewBox="0 0 13 11"><path d="M0 1h2.5l2 6h6.5l1.5-4.5H4" stroke="#333" stroke-width="1.6" fill="none"/><circle cx="5" cy="9.5" r="1.2" fill="#333"/><circle cx="10" cy="9.5" r="1.2" fill="#333"/></svg>0,00 €</span>
  </div>
  <div class="main-nav"><span>Sonderangebote</span><span class="caret">Pool &amp; Zubehör</span><span class="caret">Sauna</span><span class="caret">Infrarot</span><span>Holzbadewannen</span></div>

  <svg class="hero" viewBox="0 0 1095 369" aria-label="Aktionsbanner: Holzpools sofort lieferbar">
    <defs>
      <linearGradient id="garden" x1="0" y1="0" x2="0" y2="1">
        <stop offset="0" stop-color="#cfe3f0"/><stop offset="0.35" stop-color="#6f8f4a"/>
        <stop offset="0.55" stop-color="#4a87b8"/><stop offset="0.8" stop-color="#b48a5c"/><stop offset="1" stop-color="#8a6a44"/>
      </linearGradient>
    </defs>
    <rect width="1095" height="369" fill="var(--navy)"/>
    <polygon points="505,0 1095,0 1095,369 495,369 440,185" fill="url(#garden)" role="img" aria-label="Foto: Holzpool mit Holzdeck im Garten vor einem Haus"/>
    <polyline points="505,0 440,185 495,369" fill="none" stroke="#fff" stroke-width="14"/>
    <g font-family="'Open Sans',Arial,sans-serif" font-weight="800">
      <text x="48" y="99" font-size="31" fill="#fff">VERSCHÖNERN SIE</text>
      <text x="48" y="135" font-size="31" fill="#fff">DOCH IHREN GARTEN</text>
      <text x="46" y="205" font-size="52" fill="var(--banner-cyan)">HOLZPOOLS</text>
      <text x="46" y="253" font-size="52" fill="var(--banner-cyan)">SOFORT</text>
      <text x="46" y="301" font-size="52" fill="var(--banner-cyan)">LIEFERBAR!</text>
    </g>
    <rect x="869" y="144" width="217" height="217" fill="var(--navy-deep)"/>
    <rect x="916" y="168" width="26" height="26" fill="var(--banner-cyan)"/>
    <g font-family="Montserrat,Arial,sans-serif" font-weight="900" font-size="34">
      <text x="920" y="233" fill="#fff">STAY</text>
      <text x="920" y="262" fill="#fff">HOME</text>
      <text x="920" y="291" fill="var(--banner-cyan)">SAVE</text>
      <text x="920" y="320" fill="var(--banner-cyan)">LIVES</text>
    </g>
  </svg>

  <div class="slider-dots"><i></i><i class="active"></i><i></i><i></i><i></i></div>
  <div class="divider"></div>
  <h2 class="section-title">Unsere TOP-Kategorien</h2>

  <div class="category" style="left:42px"><div class="photo" role="img" aria-label="Foto: achteckiger Holzpool auf Holzdeck im Garten" style="background:linear-gradient(#4f7a3a,#3f8bc6 55%,#a07c52 75%,#5f8f3a)"></div>Holzpools</div>
  <div class="category" style="left:369px"><div class="photo" role="img" aria-label="Foto: blaue Poolabdeckung auf gepflastertem Rand" style="background:linear-gradient(90deg,#9a9a92 0 10%,#1fa0e6 18%,#2aa8ea 82%,#8a8a84 90%)"></div>Poolabdeckungen</div>
  <div class="category" style="left:697px"><div class="photo" role="img" aria-label="Foto: Pool mit aufgerollter Oberflur-Rollladenabdeckung" style="background:linear-gradient(160deg,#3d4a36,#b9d6e6 35%,#2f6fd6 65%,#9a9c96)"></div>Oberflur</div>
</div>
</body>
</html>
```